Biz cards

Need some business cards to handout when finding clients for medical marijuana

Industry/Entity Type

Business

Contact Information for Business Card

Name: Dev Tolland
Cell #604-555-0193
Instagram: lunarvalleyfarmsbc

Requirements
Must have
• Needs to say ( on back of card with my info )
• MMAR Producer
• Marijuana Enthusiest and connoisseur

```html
<!DOCTYPE html>
<html lang="en">
<head>
<meta charset="utf-8">
<title>Lunar Valley Farms – Business Cards</title>
<link href="https://fonts.googleapis.com/css2?family=Montserrat:wght@500;600;700;800&display=swap" rel="stylesheet">
<style>
  :root {
    --stage: #2b2b2d;
    --card-black: #050505;
    --card-white: #ffffff;
    --ink: #111111;
    --brand-red: #e3262b;
    --white: #ffffff;
  }
  * { box-sizing: border-box; margin: 0; padding: 0; }
  html, body { width: 1200px; height: 880px; overflow: hidden; }
  body {
    background: var(--stage);
    font-family: "Montserrat", sans-serif;
    display: flex;
    flex-direction: column;
    align-items: center;
    justify-content: center;
    gap: 36px;
  }
  .card {
    width: 700px;
    height: 400px;
    border-radius: 22px;
    position: relative;
    overflow: hidden;
  }
  /* Back side */
  .card--back {
    background: var(--card-black);
    display: flex;
    align-items: center;
    justify-content: center;
  }
  .brand {
    display: flex;
    align-items: center;
    gap: 14px;
  }
  .brand__dot {
    width: 22px; height: 22px;
    border-radius: 50%;
    flex: none;
  }
  .brand__name {
    font-weight: 800;
    text-transform: uppercase;
    letter-spacing: 1px;
    line-height: 1.05;
    white-space: nowrap;
  }
  .card--back .brand__dot { background: var(--white); }
  .card--back .brand__name { color: var(--white); font-size: 40px; }

  /* Front side */
  .card--front { background: var(--card-white); }
  .front__logo-area {
    position: absolute;
    left: 0; top: 140px;
    width: 390px;
    display: flex;
    justify-content: center;
  }
  .card--front .brand__dot { background: var(--brand-red); width: 20px; height: 20px; }
  .card--front .brand__name { color: var(--ink); font-size: 27px; }
  .front__divider {
    position: absolute;
    left: 400px; top: 70px;
    width: 1px; height: 190px;
    background: var(--brand-red);
  }
  .front__info {
    position: absolute;
    left: 436px; top: 78px;
  }
  .person__name {
    font-weight: 800;
    font-size: 26px;
    color: var(--ink);
    text-transform: uppercase;
    letter-spacing: 0.5px;
  }
  .person__title {
    font-weight: 600;
    font-size: 17px;
    color: var(--brand-red);
    margin-top: 2px;
  }
  .contact {
    list-style: none;
    margin-top: 36px;
    display: flex;
    flex-direction: column;
    gap: 10px;
  }
  .contact__item {
    display: flex;
    align-items: center;
    gap: 10px;
    font-weight: 600;
    font-size: 16px;
    color: var(--ink);
  }
  .contact__item--phone { font-size: 20px; font-weight: 700; }
  .contact__icon { width: 24px; height: 24px; flex: none; }
  .front__band {
    position: absolute;
    left: 0; right: 0; bottom: 0;
    height: 58px;
    background: var(--brand-red);
    display: flex;
    align-items: center;
    padding: 0 26px;
    gap: 20px;
  }
  .band__badge {
    width: 30px; height: 30px;
    border-radius: 50%;
    background: var(--white);
    flex: none;
  }
  .band__tagline {
    color: var(--white);
    font-weight: 700;
    font-size: 18px;
    letter-spacing: 0.8px;
    flex: 1;
    padding-left: 60px;
  }
</style>
</head>
<body>

  <section class="card card--back" aria-label="Card back">
    <div class="brand">
      <span class="brand__dot"></span>
      <span class="brand__name">Lunar Valley<br>Farms</span>
    </div>
  </section>

  <section class="card card--front" aria-label="Card front">
    <div class="front__logo-area">
      <div class="brand">
        <span class="brand__dot"></span>
        <span class="brand__name">Lunar Valley<br>Farms</span>
      </div>
    </div>

    <div class="front__divider"></div>

    <div class="front__info">
      <h1 class="person__name">Dev Tolland</h1>
      <p class="person__title">MMAR Producer</p>
      <ul class="contact">
        <li class="contact__item contact__item--phone">
          <svg class="contact__icon" viewBox="0 0 24 24" aria-hidden="true">
            <rect x="7" y="3" width="10" height="18" rx="2" fill="none" stroke="#e3262b" stroke-width="1.8"/>
            <line x1="10.5" y1="18" x2="13.5" y2="18" stroke="#e3262b" stroke-width="1.6"/>
          </svg>
          604-555-0193
        </li>
        <li class="contact__item">
          <svg class="contact__icon" viewBox="0 0 24 24" aria-hidden="true">
            <circle cx="12" cy="12" r="8" fill="none" stroke="#e3262b" stroke-width="1.8"/>
          </svg>
          lunarvalleyfarmsbc
        </li>
      </ul>
    </div>

    <div class="front__band">
      <span class="band__badge"></span>
      <span class="band__tagline">Marijuana Enthusiest and connoisseur</span>
      <span class="band__badge"></span>
    </div>
  </section>

</body>
</html>
```